Brand Business Card for Hotel Cloud Management System

Hello designers,
we are looking for a new brand business card for our product Stayvora. Our brand Stayvora is a hotel management system for small hotels, B&B, guesthouses etc. and just recently we are expanding our offer to other European markets. Therefore we need a business card that will communicate not only to the end-users (hoteliers) but also to potential business partners/ We would like the brand business card to be professional looking, but not too serius, modern, elegant, clean, Our brand color is orange, dark grey and it would be nice to see both combined.

Please visit our website www.stayvora.eu to get more impression on what our brand stayvora stands for.

Please find attached stayvora logo.

Target Market(s)

small hotels, hoteliers, B&B owners, potential business partners

Industry/Entity Type

Software Service

Contact Information for Business Card

Stayvora
- hotel software solutions - web booking engine - multi channel manager
www.stayvora.eu
T: +38614738265
E: info@stayvora.net

Font styles to use
Serif
Sans Serif

Colors
f37122
aaaaaa
606060
f6f6f6

Requirements
Must have
• Logo of the brand
• the layout of the business card should be in connection with the look and feel of the website stayvora.eu and logo stayvora;

```html
<!DOCTYPE html>
<html lang="en">
<head>
<meta charset="utf-8">
<title>Stayvora Business Card</title>
<link href="https://fonts.googleapis.com/css2?family=Lato:wght@300;400;900&display=swap" rel="stylesheet">
<style>
  :root {
    --brand-orange: #f37122;
    --brand-orange-deep: #e07a2c;
    --ink: #1c1c1c;
    --ink-soft: #606060;
    --paper: #ffffff;
    --stage: #3a3b3e;
  }
  * { box-sizing: border-box; margin: 0; padding: 0; }
  html, body {
    width: 1200px; height: 900px; overflow: hidden;
    background: var(--stage);
    font-family: "Lato", Arial, sans-serif;
  }
  .card {
    position: absolute; left: 240px;
    width: 720px; height: 411px;
    background: var(--paper);
    overflow: hidden;
    box-shadow: 0 10px 24px rgba(0,0,0,.35);
  }
  .card--front { top: 26px; }
  .card--back { top: 463px; }

  .brand-name {
    position: absolute; left: 0; right: 0;
    text-align: center;
    font-weight: 900;
    color: var(--ink);
    letter-spacing: -1px;
  }
  .card--front .brand-name { top: 120px; font-size: 86px; }
  .card--back .brand-name { top: 54px; font-size: 60px; }

  .services {
    position: absolute; left: 0; right: 0; bottom: 44px;
    text-align: center;
    font-weight: 900; font-size: 17px;
    color: var(--ink);
    letter-spacing: .3px;
  }
  .services .star { color: var(--brand-orange); margin: 0 6px; }

  .contact {
    position: absolute; left: 236px; top: 178px;
    font-weight: 300; font-size: 25px; color: var(--ink);
    list-style: none;
  }
  .contact li { display: flex; align-items: center; height: 40px; }
  .contact .icon {
    width: 30px; height: 30px; border-radius: 50%;
    background: var(--brand-orange);
    display: inline-flex; align-items: center; justify-content: center;
    margin-right: 14px;
  }
  .contact .web {
    font-weight: 900; color: var(--brand-orange);
    letter-spacing: 2px; padding-left: 44px;
  }
  .swoosh { position: absolute; left: 0; top: 0; }
</style>
</head>
<body>
  <section class="card card--front">
    <div class="brand-name">Stayvora</div>
    <p class="services">Hotel Software Solutions<span class="star">★</span>Web Booking Engine<span class="star">★</span>Multi Channel Manager</p>
  </section>

  <section class="card card--back">
    <div class="brand-name">Stayvora</div>
    <ul class="contact">
      <li><span class="icon">
        <svg width="16" height="16" viewBox="0 0 24 24"><path fill="#fff" d="M6.6 10.8a15 15 0 0 0 6.6 6.6l2.2-2.2c.3-.3.7-.4 1-.2 1.1.4 2.3.6 3.6.6.6 0 1 .4 1 1V20c0 .6-.4 1-1 1A17 17 0 0 1 3 4c0-.6.4-1 1-1h3.5c.6 0 1 .4 1 1 0 1.3.2 2.5.6 3.6.1.3 0 .7-.2 1z"/></svg>
      </span>+38614738265</li>
      <li><span class="icon">
        <svg width="16" height="16" viewBox="0 0 24 24"><rect x="3" y="6" width="18" height="12" rx="1" fill="none" stroke="#fff" stroke-width="2"/><path d="M3 7l9 6 9-6" fill="none" stroke="#fff" stroke-width="2"/></svg>
      </span>info@stayvora.net</li>
      <li class="web">www.stayvora.eu</li>
    </ul>
    <svg class="swoosh" width="720" height="411" viewBox="0 0 720 411" aria-hidden="true">
      <path fill="var(--brand-orange-deep)" d="M0 411 L0 388 C260 372 560 300 720 205 L720 411Z"/>
      <path fill="var(--ink)" d="M290 360 C480 322 640 250 720 160 L720 188 C640 268 480 335 290 360Z"/>
    </svg>
  </section>
</body>
</html>
```